Website Landing Page for Brightfall Systems

Create a custom designed website landing page for our business. Looking for a professional upscale design that incorporates our logo and logo colors into the theme. I want a standard fixed frame website, not a constant scrolling format that seems to be the trend. To start with I'm looking for more of the graphic design part, maybe a concept or theme, I don't expect to see a finished project. Not interested in generic templates or layouts.

The name of our company is Brightfall Systems and I've attached our logo below. I'd like to have the web page have the same look and feel of our logo, as well as the colors. Our company, Brightfall Systems does system design, installation, and programming, of residential and commercial Audio/Video and Automation systems. We do home theaters, lighting and building automation, video conferencing systems, security camera installations, conference rooms, projectors, distributed audio systems, and similar Technology projects. This will be a professional services/informational website. We will not sell products on this website. This website will be used to advertise our company and communicate our services to prospective customers. Having a well designed, professional and clean website is one way we want to distinguish our company from the competition.

Here are some examples of what I consider a professional well designed website
http://www.qorlamstudio.com/Work/

Last year we had our tradlo store designed (with PixelMarket) and I'm really happy with the way it turned out. You can see it at www.HolvenGearDepot.com I consider this to be a great design and looking for the same level of quality with this new website. However, do not copy or use any part of this design in this new project. This tradlo store is completely separate from our other company Brightfall Systems. I only mention this tradlo store an an example of good work.

Reason: Still going through designs.

Reason: Still working on project and have not had time to review all designs and request revisions.

Reason: Sill going through designs and requesting revisions

Reason: still going through all the submissions we received.

Target Market(s)

People interested in Audio/Video, home theaters, home automation. We do sales, system design, and programming. We typically work on larger projects with both residential and commercial customers.

Industry/Entity Type

Business

Number of Pages Required

1 page

Requirements
Must have
• Great design elements. Please use a white background. I think white goes well with our logo colors.

```html
<!DOCTYPE html>
<html lang="en">
<head>
<meta charset="utf-8">
<title>Brightfall Systems</title>
<link rel="stylesheet" href="https://fonts.googleapis.com/css2?family=Gilda+Display&family=Work+Sans:wght@400;600&display=swap">
<style>
  :root {
    --navy: #2b417c;
    --navy-light: #2f5aa0;
    --blue: #1466c4;
    --blue-band: #1d55aa;
    --green: #46b866;
    --sky: #d6f5fb;
    --sky-pale: #ecfbfe;
    --sky-deep: #a9eef8;
    --mint: #d4f6df;
    --white: #ffffff;
    --ink: #4a4d57;
    --body: #5a5d66;
    --accent: #2b8cf0;
    --serif: "Gilda Display", Georgia, serif;
    --sans: "Work Sans", Helvetica, Arial, sans-serif;
  }
  * { box-sizing: border-box; margin: 0; padding: 0; }
  html, body { width: 1107px; height: 1200px; overflow: hidden; background: var(--white); }
  .page { position: relative; width: 1107px; height: 1200px; overflow: hidden; font-family: var(--sans); }
  .backdrop { position: absolute; inset: 0; }

  .nav { position: absolute; top: 22px; left: 0; width: 100%; height: 16px; }
  .nav a { position: absolute; color: var(--white); font-size: 10px; font-weight: 600; text-decoration: none; }
  .nav .services { left: 352px; }
  .nav .works { left: 424px; }
  .nav .about { left: 654px; }
  .nav .contact { left: 715px; }

  .brand { position: absolute; left: 500px; top: 20px; width: 106px; text-align: center; }
  .brand-mark { display: block; width: 22px; height: 22px; margin: 0 auto 6px; border: 3px solid var(--green); border-radius: 50%; }
  .brand-name { display: block; font-family: var(--sans); font-weight: 600; font-size: 7.5px; line-height: 8.5px; letter-spacing: .4px; color: var(--green); text-transform: uppercase; }

  .hero { position: absolute; top: 211px; left: 0; width: 100%; text-align: center; }
  .hero h1 { font-family: var(--serif); font-weight: 400; font-size: 30px; line-height: 35px; color: var(--white); }
  .watch { display: inline-flex; align-items: center; gap: 10px; margin-top: 26px; color: var(--white); font-size: 10px; font-weight: 600; letter-spacing: 1px; text-decoration: none; }

  .intro { position: absolute; top: 838px; left: 0; width: 100%; text-align: center; }
  .intro h2 { font-family: var(--serif); font-weight: 400; font-size: 31px; line-height: 40px; color: var(--ink); margin-bottom: 30px; }
  .intro p { font-size: 10.4px; line-height: 17.5px; color: var(--body); margin: 0 auto 17px; }
  .intro .lead { width: 300px; }
  .intro .second { width: 250px; }
  .intro .name { color: var(--accent); }
  .btn { display: inline-block; margin-top: 22px; width: 115px; height: 28px; line-height: 28px; background: var(--accent); color: var(--white); font-size: 10px; font-weight: 600; letter-spacing: 1px; text-decoration: none; border-radius: 2px; }

  .footer { position: absolute; top: 1170px; left: 216px; width: 676px; height: 14px; }
  .copyright { font-size: 8px; color: var(--body); line-height: 14px; }
  .social { position: absolute; right: 0; top: 1px; display: flex; gap: 17px; }
  .social span { display: block; width: 12px; height: 12px; background: #6b6f7a; border-radius: 1px; }
</style>
</head>
<body>
<div class="page">
  <svg class="backdrop" width="1107" height="1200" viewBox="0 0 1107 1200">
    <defs>
      <linearGradient id="building" x1="0" y1="0" x2="0" y2="1">
        <stop offset="0" stop-color="#2c3f78"/>
        <stop offset="1" stop-color="#27498f"/>
      </linearGradient>
      <linearGradient id="roomLeft" x1="0" y1="0" x2="1" y2="1">
        <stop offset="0" stop-color="#c9d77a"/>
        <stop offset=".55" stop-color="#8fae84"/>
        <stop offset="1" stop-color="#6a7f98"/>
      </linearGradient>
      <linearGradient id="roomCenter" x1="0" y1="0" x2="0" y2="1">
        <stop offset="0" stop-color="#7a6763"/>
        <stop offset=".55" stop-color="#5d5a5e"/>
        <stop offset="1" stop-color="#9aa9a6"/>
      </linearGradient>
      <linearGradient id="roomRight" x1="0" y1="0" x2="0" y2="1">
        <stop offset="0" stop-color="#c7d96e"/>
        <stop offset=".4" stop-color="#6f9a6d"/>
        <stop offset=".7" stop-color="#6b6a5e"/>
        <stop offset="1" stop-color="#a3b5a4"/>
      </linearGradient>
    </defs>

    <rect width="1107" height="1200" fill="var(--sky)"/>

    <g role="img" aria-label="Dome of a modern office building seen from below">
      <polygon points="0,0 1107,0 1107,640 553,760 0,500" fill="url(#building)"/>
    </g>
    <polygon points="308,0 553,149 788,0" fill="var(--navy-light)" opacity=".8"/>
    <polygon points="553,149 853,342 553,530 260,342" fill="var(--blue-band)" opacity=".45"/>
    <polygon points="0,248 198,376 0,500" fill="var(--blue)"/>
    <polygon points="1107,178 853,342 1107,502" fill="var(--green)"/>

    <polygon points="0,500 198,608 320,608 553,754 853,790 1107,628 1107,1200 0,1200" fill="var(--sky)"/>
    <polygon points="0,880 200,760 553,970 200,1200 0,1200" fill="var(--sky-pale)"/>
    <polygon points="1107,840 920,960 1107,1120" fill="var(--sky-pale)"/>
    <polygon points="188,920 553,700 922,920 922,1200 188,1200" fill="#d9f7fc" opacity=".7"/>
    <polygon points="0,1120 188,1000 500,1200 0,1200" fill="var(--mint)" opacity=".6"/>
    <polygon points="188,1000 500,1200 188,1200" fill="var(--sky-deep)" opacity=".7"/>
    <polygon points="440,1200 640,1036 800,1140 720,1200" fill="var(--white)"/>
    <polygon points="610,1200 922,1000 1107,1120 1107,1200" fill="var(--mint)" opacity=".8"/>
    <polygon points="922,1000 1107,1120 1107,1200 922,1200" fill="var(--sky-deep)"/>

    <g role="img" aria-label="Living room with a wall-mounted screen showing a waterfall">
      <polygon points="0,500 198,376 384,490 264,574 320,608 198,680 198,608" fill="url(#roomLeft)"/>
    </g>
    <g role="img" aria-label="Conference room with a long table and wall display">
      <polygon points="264,574 553,386 792,540 624,648 553,688 553,754" fill="url(#roomCenter)"/>
    </g>
    <g role="img" aria-label="Home theater lounge with a large screen and speakers">
      <polygon points="853,342 1107,502 1107,628 853,790 624,648 792,540 668,460" fill="url(#roomRight)"/>
    </g>

    <polygon points="488,0 502,70 553,108" fill="var(--green)"/>
    <polygon points="620,0 606,70 553,108" fill="var(--blue)"/>
    <polygon points="488,0 620,0 606,70 553,100 502,70" fill="#f3f7fa"/>
  </svg>

  <nav class="nav">
    <a class="services" href="#">Services</a>
    <a class="works" href="#">Works</a>
    <a class="about" href="#">About</a>
    <a class="contact" href="#">Contact</a>
  </nav>

  <div class="brand">
    <span class="brand-mark"></span>
    <span class="brand-name">Brightfall<br>Systems</span>
  </div>

  <section class="hero">
    <h1>We offer professional services<br>including system design.</h1>
    <a class="watch" href="#">
      <svg width="7" height="8" viewBox="0 0 7 8"><polygon points="1,1 6,4 1,7" fill="none" stroke="#fff" stroke-width="1.3"/></svg>
      WATCH VIDEO
    </a>
  </section>

  <section class="intro">
    <h2>Introduction</h2>
    <p class="lead"><span class="name">Brightfall Systems</span> is an innovative company that offers custom designed automation systems and a wide range of Pro Audio/Video products at wholesale prices.</p>
    <p class="second">We offer a huge selection of products from all the top manufacturers in the industry.</p>
    <a class="btn" href="#">ABOUT US</a>
  </section>

  <footer class="footer">
    <span class="copyright">© Brightfall Systems</span>
    <div class="social"><span></span><span></span><span></span></div>
  </footer>
</div>
</body>
</html>
```